Business cards for the RL Group

We are looking for a template for our new business cards for our company that we can edit ourselves.
You will find our company colors in the logo. the logo on the back and on the front
first name Last Name
position
E-mail address
mobile number
landline number
Companies we have 2 RL Sicherheit GmbH and RL Services GmbH
address
Lindenbergweg 42
22459 Hamburg
www.rlgruppe-nord.de

Something modern, simple but professional

if you have any questions, bring it on.

Sicherheit

Steht in der Beschreibung

F0912C
F2A743
F7CA91
FBE8D2
FDF5EE

• recognition value
• professional
• Playful

```html
<!DOCTYPE html>
<html lang="de">
<head>
<meta charset="utf-8">
<title>RL Gruppe – Visitenkarten</title>
<link href="https://fonts.googleapis.com/css2?family=Montserrat:wght@400;500;700;800&display=swap" rel="stylesheet">
<style>
  :root{
    --bg:#2a2a2a;
    --card-dark:#595959;
    --card-light:#ffffff;
    --ink:#555555;
    --ink-soft:#6a6a6a;
    --orange:#F0912C;
    --white:#ffffff;
    --rule:#444444;
  }
  *{box-sizing:border-box;margin:0;padding:0}
  html,body{width:1200px;height:866px;overflow:hidden}
  body{
    background:var(--bg);
    font-family:"Montserrat",sans-serif;
    display:flex;align-items:center;justify-content:center;gap:30px;
  }
  .card{
    width:560px;height:320px;position:relative;overflow:hidden;
    box-shadow:0 10px 30px rgba(0,0,0,.45);
  }
  /* back side */
  .card--back{background:var(--card-dark);display:flex;align-items:center;justify-content:center}
  .brand{display:flex;align-items:center;gap:12px;white-space:nowrap}
  .brand__mark{width:22px;height:22px;border-radius:50%;background:var(--orange);flex:none}
  .brand__name{font-weight:800;font-size:48px;letter-spacing:1px;line-height:1}
  .card--back .brand__name{color:var(--white)}
  /* front side */
  .card--front{background:var(--card-light)}
  .card--front .brand{position:absolute;left:40px;top:92px}
  .card--front .brand__name{color:var(--ink);font-size:32px;letter-spacing:.5px}
  .card--front .brand__mark{width:16px;height:16px}
  .person{position:absolute;right:36px;top:54px;width:210px;text-align:right}
  .person__name{font-weight:800;font-size:21px;color:var(--ink);letter-spacing:.5px;white-space:nowrap}
  .person__role{font-weight:500;font-size:13px;color:var(--ink);margin-top:4px;padding-bottom:10px;border-bottom:1px solid var(--rule)}
  .person__address{font-size:13px;color:var(--ink-soft);margin-top:14px;line-height:1.5}
  .contact{position:absolute;left:40px;bottom:24px;width:250px;border-top:1px solid var(--rule);padding-top:10px}
  .contact__row{display:flex;align-items:center;gap:10px;font-size:14px;color:var(--ink);line-height:1.65;white-space:nowrap}
  .contact__icon{width:14px;height:14px;flex:none;fill:var(--orange)}
</style>
</head>
<body>
  <section class="card card--back">
    <div class="brand">
      <span class="brand__mark"></span>
      <span class="brand__name">RL Gruppe</span>
    </div>
  </section>

  <section class="card card--front">
    <div class="brand">
      <span class="brand__mark"></span>
      <span class="brand__name">RL Gruppe</span>
    </div>

    <div class="person">
      <div class="person__name">MARTIN KELLER</div>
      <div class="person__role">Managing Director</div>
      <div class="person__address">Lindenbergweg 42<br>22459 Hamburg</div>
    </div>

    <div class="contact">
      <div class="contact__row">
        <svg class="contact__icon" viewBox="0 0 24 24"><path d="M6.6 10.8a15 15 0 0 0 6.6 6.6l2.2-2.2a1 1 0 0 1 1-.25 11 11 0 0 0 3.6.6 1 1 0 0 1 1 1V20a1 1 0 0 1-1 1A17 17 0 0 1 3 4a1 1 0 0 1 1-1h3.5a1 1 0 0 1 1 1 11 11 0 0 0 .6 3.6 1 1 0 0 1-.25 1z"/></svg>
        <span>040-555 218 304</span>
      </div>
      <div class="contact__row">
        <svg class="contact__icon" viewBox="0 0 24 24"><path d="M3 8c0-2 4-4 9-4s9 2 9 4v2h-5V8H8v2H3zM6 11h12l2 9H4zm6 2.5a2.5 2.5 0 1 0 0 5 2.5 2.5 0 0 0 0-5z"/></svg>
        <span>040-555 218 300</span>
      </div>
      <div class="contact__row">
        <svg class="contact__icon" viewBox="0 0 24 24"><path d="M2 5h20v14H2zm2 2v.5l8 5.5 8-5.5V7l-8 5.5z"/></svg>
        <span>info@rlgruppe-nord.de</span>
      </div>
      <div class="contact__row">
        <svg class="contact__icon" viewBox="0 0 24 24"><path d="M12 2a10 10 0 1 0 0 20 10 10 0 0 0 0-20zm-1 17.9A8 8 0 0 1 4.1 11H7v2l4 4zm6.9-2.5A2 2 0 0 0 16 16h-1v-3a1 1 0 0 0-1-1H8v-2h2a1 1 0 0 0 1-1V7h2a2 2 0 0 0 2-2v-.4a8 8 0 0 1 2.9 12.8z"/></svg>
        <span>www.rlgruppe-nord.de</span>
      </div>
    </div>
  </section>
</body>
</html>
```